Business card for different employees

A professional new updated design incorporating our current business's color themes and styles such as our on-site service trucks decals included in pictures attached. Our current business card is very simple and not professionally designed. We are a small family business but want a professional corporate look.

Target Market(s)

Cards to be handed out to new customers , corperate meetings. For our on site service operators.

Industry/Entity Type

Hydraulic

Contact Information for Business Card

Address, website, phone number, email, logo.
slogan - "Industry chosen hose and fittings provider".
24/7 on-site service , supply and hose management
Experienced , indpendant , family owned

Font styles to use
Sans Serif

Requirements
Must have
• Easily editable so that I can add different names and different roles for employees etc.
Nice to have
• Freedom with colour doesn't necessarily have to be blue but that is our company colour theme with trucks and logo so makes sense for the card to have blue like the trucks.

```html
<!DOCTYPE html>
<html lang="en">
<head>
<meta charset="UTF-8">
<title>Meridian Hose Supply – Business Card</title>
<link href="https://fonts.googleapis.com/css2?family=Jost:wght@400;500;700&display=swap" rel="stylesheet">
<style>
  :root {
    --brand-blue: #3346a1;
    --brand-blue-light: #4a5db3;
    --ink: #2b2b2b;
    --paper: #ffffff;
    --backdrop: #2a2a2c;
    --rule: rgba(255,255,255,0.85);
  }
  * { margin: 0; padding: 0; box-sizing: border-box; }
  html, body {
    width: 1200px; height: 960px; overflow: hidden;
    background: var(--backdrop);
    font-family: "Jost", Arial, sans-serif;
  }
  .sheet {
    width: 1200px; height: 960px;
    display: flex; flex-direction: column; align-items: center; justify-content: center;
    gap: 44px;
  }
  .card {
    width: 700px; height: 400px;
    border-radius: 26px;
    position: relative;
    overflow: hidden;
    box-shadow: 0 10px 24px rgba(0,0,0,0.45);
  }
  /* ---- Front (blue) ---- */
  .card--front {
    background: linear-gradient(135deg, var(--brand-blue-light) 0%, var(--brand-blue) 55%);
    color: #fff;
  }
  .wordmark {
    display: flex; align-items: center; gap: 14px;
    font-weight: 700; letter-spacing: 0.04em; text-transform: uppercase;
    white-space: nowrap;
  }
  .wordmark__dot {
    width: 30px; height: 30px; border-radius: 50%;
    background: var(--ink); flex: none;
  }
  .card--front .wordmark {
    position: absolute; top: 92px; left: 0; right: 0; justify-content: center;
    font-size: 44px; color: #fff;
  }
  .card--front .wordmark__dot { background: #1d1d1f; }
  .services {
    position: absolute; top: 196px; left: 0; right: 0;
    text-align: center; font-size: 21px; line-height: 1.45; font-weight: 400;
  }
  .services li { list-style: none; }
  .services span::before { content: "• "; }
  .services span + span { margin-left: 14px; }
  .slogan {
    position: absolute; bottom: 52px; left: 0; right: 0;
    display: flex; align-items: center; gap: 18px;
    font-size: 22px; white-space: nowrap;
  }
  .slogan::before, .slogan::after {
    content: ""; flex: 1; height: 1.5px; background: var(--rule);
  }
  /* ---- Back (white) ---- */
  .card--back { background: var(--paper); color: var(--ink); }
  .card--back .wordmark {
    position: absolute; top: 62px; left: 0; right: 0; justify-content: center;
    font-size: 44px; color: var(--brand-blue);
  }
  .details {
    position: absolute; top: 172px; left: 60px; right: 40px;
    display: flex; align-items: center;
  }
  .person { text-align: right; padding-right: 26px; flex: 1; }
  .person__name {
    font-size: 34px; font-weight: 700; color: var(--brand-blue);
    text-transform: uppercase; letter-spacing: 0.02em; line-height: 1.1;
  }
  .person__role { font-size: 20px; color: #444; }
  .divider { width: 2px; height: 96px; background: var(--brand-blue); flex: none; }
  .contact { padding-left: 26px; flex: 1.5; font-size: 19px; line-height: 1.6; }
  .contact li { list-style: none; display: flex; align-items: center; gap: 10px; white-space: nowrap; }
  .contact svg { width: 16px; height: 16px; fill: var(--brand-blue); flex: none; }
  .contact .link { color: var(--brand-blue); }
  .address {
    position: absolute; bottom: 56px; left: 0; right: 0;
    text-align: center; font-size: 21px; color: #333;
  }
</style>
</head>
<body>
<main class="sheet">

  <section class="card card--front" aria-label="Business card front">
    <div class="wordmark"><span class="wordmark__dot"></span>Meridian Hose Supply</div>
    <ul class="services">
      <li><span>Supply and Hose Management</span><span>24/7 on-site service</span></li>
      <li><span>Experienced</span><span>Indpendant</span><span>Family Owned</span></li>
    </ul>
    <p class="slogan">Industry Chosen Hose And Fittings Provider</p>
  </section>

  <section class="card card--back" aria-label="Business card back">
    <div class="wordmark"><span class="wordmark__dot"></span>Meridian Hose Supply</div>
    <div class="details">
      <div class="person">
        <p class="person__name">Daniel Reyes</p>
        <p class="person__role">Owner/CEO</p>
      </div>
      <div class="divider"></div>
      <ul class="contact">
        <li>
          <svg viewBox="0 0 24 24" aria-hidden="true"><path d="M6.6 10.8a15.1 15.1 0 0 0 6.6 6.6l2.2-2.2a1 1 0 0 1 1-.25 11.4 11.4 0 0 0 3.6.57 1 1 0 0 1 1 1V20a1 1 0 0 1-1 1A17 17 0 0 1 3 4a1 1 0 0 1 1-1h3.5a1 1 0 0 1 1 1c0 1.25.2 2.45.57 3.6a1 1 0 0 1-.25 1z"/></svg>
          555-018-2740
        </li>
        <li>
          <svg viewBox="0 0 24 24" aria-hidden="true"><path d="M2 5h20v14H2z M4 7v.5l8 5 8-5V7l-8 5z" fill-rule="evenodd"/></svg>
          info@meridianhosesupply.com
        </li>
        <li>
          <svg viewBox="0 0 24 24" aria-hidden="true"><circle cx="12" cy="12" r="10"/></svg>
          <span>www.<span class="link">meridianhosesupply</span>.com</span>
        </li>
      </ul>
    </div>
    <p class="address">1840 B Harlow Avenue Westbrook County 6140</p>
  </section>

</main>
</body>
</html>
```